Edit current business card design

Need business card design where Business Name, Logo, Address, phone and fax, website address are permanent.Need to be able to add and edit employee name and email address.

Business

```html
<!DOCTYPE html>
<html lang="en">
<head>
<meta charset="utf-8">
<title>Marlow's Accounting Service – Business Card</title>
<link rel="stylesheet" href="https://fonts.googleapis.com/css2?family=Didact+Gothic&family=Lato:ital,wght@0,400;0,700;0,900;1,400&display=swap">
<style>
  :root{
    --backdrop:#8fd9a2;
    --green-dark:#3f6b49;
    --green-mid:#5e8a67;
    --green-light:#8cb596;
    --card-white:#ffffff;
    --card-grey:#d9dbd9;
    --ink:#1b1f1c;
    --ink-soft:#3a3f3b;
    --on-green:#ffffff;
  }
  *{box-sizing:border-box;margin:0;padding:0}
  html,body{width:800px;height:1200px;overflow:hidden}
  body{background:var(--backdrop);position:relative;font-family:"Lato",sans-serif}
  .card{position:absolute;left:80px;width:640px;height:366px;overflow:hidden;box-shadow:0 10px 30px rgba(0,0,0,.18)}
  .card--front{top:150px;background:linear-gradient(160deg,var(--card-white) 45%,var(--card-grey) 100%)}
  .card--back{top:640px;background:radial-gradient(ellipse at 55% 50%,var(--green-light) 0%,var(--green-mid) 55%,var(--green-dark) 100%)}
  .card__art{position:absolute;inset:0}
  .business-name{position:absolute;left:26px;top:24px;font-family:"Didact Gothic",sans-serif;font-size:27px;letter-spacing:2px;color:var(--ink)}
  .brand{position:absolute;right:30px;top:68px;display:flex;align-items:center;gap:8px}
  .brand__dot{width:30px;height:30px;border-radius:50%;background:var(--green-mid);flex:none}
  .brand__name{font-family:"Didact Gothic",sans-serif;font-size:22px;color:var(--green-dark)}
  .employee{position:absolute;left:60px;top:150px}
  .employee__name{font-weight:900;font-size:32px;color:var(--ink);letter-spacing:-.5px}
  .employee__credentials{font-size:21px;color:var(--ink-soft);margin-top:2px}
  .contact{position:absolute;left:46px;top:270px;list-style:none;color:var(--on-green);font-size:16px;line-height:27px}
  .contact li{display:flex;align-items:center;gap:9px}
  .contact svg{width:14px;height:14px;flex:none}
  .contact__web{margin-left:26px}
  .services__title{position:absolute;top:28px;left:0;right:0;text-align:center;font-family:"Didact Gothic",sans-serif;font-size:36px;letter-spacing:9px;color:var(--ink)}
  .services__list{position:absolute;left:40px;top:96px;list-style:none;font-size:18px;line-height:30px;color:var(--ink)}
  .services__list li::before{content:"•";margin-right:9px}
  .services__tagline{position:absolute;left:0;right:0;bottom:34px;text-align:center;font-size:17px;color:var(--on-green);letter-spacing:.5px}
</style>
</head>
<body>

<section class="card card--front" aria-label="Business card front">
  <svg class="card__art" viewBox="0 0 640 366" aria-hidden="true">
    <defs>
      <linearGradient id="bandFill" x1="0" y1="0" x2="1" y2="0">
        <stop offset="0" stop-color="#3f6b49"/>
        <stop offset=".55" stop-color="#5e8a67"/>
        <stop offset="1" stop-color="#8cb596"/>
      </linearGradient>
    </defs>
    <path d="M0,366 L0,262 C170,232 420,190 640,120 L640,366 Z" fill="url(#bandFill)"/>
    <path d="M300,248 C420,218 540,180 640,140 L640,150 C540,192 430,226 300,248 Z" fill="#ffffff" opacity=".35"/>
    <path d="M62,160 C130,110 220,86 330,80 C230,92 140,118 62,160 Z" fill="#3f6b49"/>
  </svg>
  <h1 class="business-name">Marlow's Accounting Service</h1>
  <div class="brand">
    <span class="brand__dot" aria-hidden="true"></span>
    <span class="brand__name">Marlow's</span>
  </div>
  <div class="employee">
    <p class="employee__name">Dale Marlow</p>
    <p class="employee__credentials">EA,ATA,ATP</p>
  </div>
  <ul class="contact">
    <li><svg viewBox="0 0 14 14"><path d="M7 1a4 4 0 0 0-4 4c0 3 4 8 4 8s4-5 4-8a4 4 0 0 0-4-4zm0 5.5A1.5 1.5 0 1 1 7 3.5a1.5 1.5 0 0 1 0 3z" fill="#fff"/></svg>418 Birchwood Ave Ste 210 Linden, GA 30412</li>
    <li><svg viewBox="0 0 14 14"><path d="M3 1l2.5 2.5-1.2 1.8a8 8 0 0 0 4.4 4.4l1.8-1.2L13 11l-1.5 2C6 13 1 8 1 2.5z" fill="#fff"/></svg>Phone: (555) 318-2740 - Fax: (555) 318-2741</li>
    <li><svg viewBox="0 0 14 14"><path d="M1 5a9 9 0 0 1 12 0M3 8a6 6 0 0 1 8 0M5 11a3 3 0 0 1 4 0" stroke="#fff" stroke-width="1.6" fill="none"/></svg>dale@marlowsacct.com<span class="contact__web">www.marlowsacct.com</span></li>
  </ul>
</section>

<section class="card card--back" aria-label="Business card back">
  <h2 class="services__title">Services</h2>
  <ul class="services__list">
    <li>Tax planning &amp; preparation for business &amp; individuals</li>
    <li>Tax problem resolutions</li>
    <li>Bookkeeping and Payroll Services</li>
    <li>Incorporation &amp; new business advisor</li>
    <li>Bookkeeping support &amp; training</li>
    <li>And more....</li>
  </ul>
  <p class="services__tagline">Helping our Clients Keep More of What They Make</p>
</section>

</body>
</html>
```